Business Cards for a law firm

Business cards for our law firm. Use our silhoette logo and OAK HARBOR - check our website (www.oakharbor-legal.com)

Contact Information for Business Card

our silhouette logo, OAK HARBOR, 800-555-0147, Dorian Kestrup, dorian@oakharbor-legal.com

Requirements
Must have
• our silhouette logo, OAK HARBOR, 800-555-0147, Dorian Kestrup, dorian@oakharbor-legal.com

```html
<!DOCTYPE html>
<html lang="en">
<head>
<meta charset="utf-8">
<title>Oak Harbor – Business Cards</title>
<link href="https://fonts.googleapis.com/css2?family=Cinzel:wght@700&family=Poppins:wght@400;600&display=swap" rel="stylesheet">
<style>
  :root {
    --navy: #22366b;
    --white: #ffffff;
    --paper: #ffffff;
  }
  * { margin: 0; padding: 0; box-sizing: border-box; }
  html, body {
    width: 1200px; height: 1200px; overflow: hidden;
    background: var(--paper);
  }
  .canvas { position: relative; width: 1200px; height: 1200px; }

  /* Front of card */
  .card-front {
    position: absolute; left: 218px; top: 120px;
    width: 771px; height: 441px;
    border: 2px solid var(--navy);
    background: var(--white);
  }
  .card-front .base-band {
    position: absolute; left: -2px; right: -2px; bottom: -2px;
    height: 23px; background: var(--navy);
  }
  .card-front .brand-mark {
    position: absolute; left: 136px; top: 190px;
    width: 36px; height: 36px; background: var(--navy);
  }
  .card-front .brand-name {
    position: absolute; left: 196px; top: 178px;
    font-family: "Cinzel", serif; font-weight: 700;
    font-size: 50px; line-height: 1; letter-spacing: 3px;
    color: var(--navy); white-space: nowrap;
  }

  /* Back of card */
  .card-back {
    position: absolute; left: 219px; top: 649px;
    width: 770px; height: 440px;
    background: var(--navy); color: var(--white);
  }
  .card-back .brand-name {
    position: absolute; left: 27px; top: 60px;
    font-family: "Cinzel", serif; font-weight: 700;
    font-size: 56px; line-height: 64px; letter-spacing: 4px;
  }
  .card-back .divider {
    position: absolute; left: 28px; top: 206px;
    width: 5px; height: 66px; background: var(--white);
  }
  .contact-list {
    position: absolute; left: 26px; top: 289px;
    list-style: none;
    font-family: "Poppins", sans-serif; font-size: 21px;
  }
  .contact-list li {
    display: flex; align-items: center; gap: 12px;
    height: 34px; margin-bottom: 2px;
  }
  .contact-list .person-name { font-weight: 600; }
  .contact-list svg { width: 19px; height: 19px; fill: var(--white); flex: none; }
</style>
</head>
<body>
<main class="canvas">

  <section class="card-front" aria-label="Card front">
    <div class="brand-mark"></div>
    <h1 class="brand-name">OAK HARBOR</h1>
    <div class="base-band"></div>
  </section>

  <section class="card-back" aria-label="Card back">
    <h2 class="brand-name">OAK<br>HARBOR</h2>
    <div class="divider"></div>
    <ul class="contact-list">
      <li class="person-name">
        <svg viewBox="0 0 20 20" aria-hidden="true"><circle cx="10" cy="5.5" r="4.5"/><path d="M1 20c0-5.5 4-8.5 9-8.5s9 3 9 8.5z"/></svg>
        Dorian Kestrup
      </li>
      <li>
        <svg viewBox="0 0 20 20" aria-hidden="true"><path d="M4.2 1.2l3 3.4c.5.6.4 1.4-.1 1.9L5.6 7.9c1.2 2.6 3.6 5 6.3 6.4l1.4-1.5c.5-.5 1.3-.6 1.9-.1l3.5 2.9c.6.5.6 1.4.1 2l-1.6 1.6C14.5 21.8 -1.4 6.7 2.4 1.3c.5-.6 1.3-.7 1.8-.1z"/></svg>
        800-555-0147
      </li>
      <li>
        <svg viewBox="0 0 20 20" aria-hidden="true"><path d="M1 4h18v12H1z M2.5 5.2v9.6l4.8-4.8z M17.5 5.2l-4.8 4.8 4.8 4.8z M3.4 4.9L10 11l6.6-6.1z M8.2 10.9l-4.9 4.3h13.4l-4.9-4.3L10 12.6z" fill-rule="evenodd"/></svg>
        dorian@oakharbor-legal.com
      </li>
    </ul>
  </section>

</main>
</body>
</html>
```